Business Card Design Project

Need a business card designed for a horse racing/gambling centered company.
Company name is BrightQuill.com.au
Company colours are similar to those in the logo.
Something clean and modern , designer given liberty to be creative.
Incorporate the logo is preferred.
Single or Double Sided fine
Must include :
Name
Mobile Number
Email Address
Reason: Apologies, I have been traveling unexpectedly with business and just need the extra two days to reply and give feedback before making a decision.
Industry/Entity Type
Business

```html
<!DOCTYPE html>
<html lang="en">
<head>
<meta charset="utf-8">
<title>BrightQuill.com.au – Business Card</title>
<link href="https://fonts.googleapis.com/css2?family=Archivo+Black&family=Arimo:ital,wght@0,700;1,700&display=swap" rel="stylesheet">
<style>
  :root {
    --page: #ffffff;
    --card: #ffffff;
    --card-edge: #b9b9b9;
    --heading-fill: #b06f45;
    --heading-stroke: #1a1a1a;
    --name-red: #8e1616;
    --ink: #2e2e2e;
    --teal: #1f9e92;
    --teal-dark: #12756c;
    --teal-pale: #e4f5f2;
  }
  * { margin: 0; padding: 0; box-sizing: border-box; }
  html, body {
    width: 1200px;
    height: 900px;
    overflow: hidden;
    background: var(--page);
  }
  .business-card {
    position: absolute;
    left: 73px;
    top: 140px;
    width: 1054px;
    height: 603px;
    background: var(--card);
    border: 1px solid var(--card-edge);
    box-shadow: 0 1px 4px rgba(0, 0, 0, 0.35);
    font-family: "Arimo", Arial, sans-serif;
  }
  .company-heading {
    position: absolute;
    right: 18px;
    top: 66px;
    font-family: "Archivo Black", "Arial Black", sans-serif;
    font-size: 50px;
    line-height: 1;
    letter-spacing: 2px;
    color: var(--heading-fill);
    -webkit-text-stroke: 3px var(--heading-stroke);
    paint-order: stroke fill;
    white-space: nowrap;
  }
  .brand-mark {
    position: absolute;
    left: 25px;
    top: 130px;
    width: 370px;
    height: 370px;
  }
  .brand-mark-name {
    position: absolute;
    left: 0;
    top: 0;
    width: 370px;
    height: 370px;
    display: flex;
    align-items: center;
    justify-content: center;
    font-family: "Arimo", Arial, sans-serif;
    font-weight: 700;
    font-size: 30px;
    color: var(--teal-dark);
  }
  .person-name {
    position: absolute;
    left: 425px;
    top: 244px;
    font-weight: 700;
    font-style: italic;
    font-size: 46px;
    letter-spacing: 1px;
    color: var(--name-red);
    white-space: nowrap;
  }
  .contact {
    position: absolute;
    font-weight: 700;
    font-size: 30px;
    letter-spacing: 1px;
    color: var(--ink);
    white-space: nowrap;
  }
  .contact-phone { right: 21px; top: 406px; }
  .contact-email { left: 23px; top: 545px; }
  .racehorse-figure {
    position: absolute;
    left: 855px;
    top: 460px;
    width: 180px;
    height: 125px;
    border-radius: 50% 40% 45% 50%;
    background: radial-gradient(ellipse at 55% 45%, rgba(31, 158, 146, 0.75), rgba(31, 158, 146, 0.15) 70%, rgba(31, 158, 146, 0) 100%);
  }
</style>
</head>
<body>
  <main class="business-card">
    <h1 class="company-heading">BRIGHTQUILL.COM.AU</h1>

    <div class="brand-mark">
      <svg width="370" height="370" viewBox="0 0 370 370" aria-hidden="true">
        <circle cx="185" cy="185" r="180" fill="var(--teal-pale)" stroke="var(--teal)" stroke-width="8"/>
      </svg>
      <span class="brand-mark-name">BrightQuill.com.au</span>
    </div>

    <p class="person-name">Mark Dalton</p>

    <p class="contact contact-phone">Phone : 0412558730</p>

    <div class="racehorse-figure" role="img" aria-label="Teal speckled silhouette of a galloping racehorse with jockey"></div>

    <p class="contact contact-email">E-mail : mark@brightquill.com.au</p>
  </main>
</body>
</html>
```